Stationery Design Project

We are looking for a full revision of our existing stationary to include within this project:

- Letterhead
- Business card
- Compliment slip

The items should be a reflection of our new website which can be found at http://www.brackenledger.co.uk/

Our logo files are included within the file brief

There are some further projects which we may approach the winning designer for as we need a revision to the front cover of our reports, a new price list and two brochures for specific target markets.

Industry/Entity Type

Business

```html
<!DOCTYPE html>
<html lang="en">
<head>
<meta charset="utf-8">
<title>Bracken Ledger Stationery</title>
<link rel="stylesheet" href="https://fonts.googleapis.com/css2?family=Nunito+Sans:wght@300;400;700&display=swap">
<style>
  :root {
    --bg: #333436;
    --paper: #ffffff;
    --navy: #111b6f;
    --blue: #1f50b8;
    --grey-text: #7a7a7a;
    --shadow: 0 8px 22px rgba(0,0,0,.45);
  }
  * { box-sizing: border-box; margin: 0; padding: 0; }
  html, body { width: 1200px; height: 1200px; overflow: hidden; }
  body {
    background: var(--bg);
    font-family: "Nunito Sans", sans-serif;
    color: var(--grey-text);
    position: relative;
  }
  .sheet {
    position: absolute;
    background: var(--paper);
    box-shadow: var(--shadow);
    overflow: hidden;
  }
  .brand-name {
    font-weight: 400;
    color: var(--navy);
    letter-spacing: .5px;
    white-space: nowrap;
  }
  .band {
    position: absolute;
    left: 0; bottom: 0;
    width: 100%;
  }
  .contacts { list-style: none; position: absolute; line-height: 1.2; }
  .contacts li { display: flex; align-items: center; white-space: nowrap; }
  .contacts svg { flex: none; }
  .contacts .hl { color: var(--navy); }
  .address { position: absolute; text-align: right; line-height: 1.25; }

  /* Letterhead */
  .letterhead { left: 40px; top: 204px; width: 560px; height: 792px; }
  .letterhead .brand-name { position: absolute; left: 40px; top: 42px; font-size: 36px; }
  .letterhead .contacts { left: 40px; bottom: 44px; font-size: 12.5px; }
  .letterhead .contacts li { gap: 7px; margin-top: 5px; }
  .letterhead .address { right: 36px; bottom: 44px; font-size: 12.5px; }

  /* Compliment slip */
  .slip { left: 640px; top: 204px; width: 520px; height: 250px; }
  .slip .brand-name { position: absolute; left: 26px; top: 26px; font-size: 27px; }
  .slip .greeting { position: absolute; left: 26px; top: 124px; font-size: 22px; font-weight: 300; line-height: 1.2; }
  .slip .greeting b { color: var(--blue); font-weight: 400; }
  .slip .contacts { left: 26px; top: 160px; font-size: 10.5px; }
  .slip .contacts li { gap: 6px; margin-bottom: 3px; }
  .slip .address { right: 18px; top: 182px; font-size: 10.5px; }

  /* Business cards */
  .card-front { left: 640px; top: 494px; width: 350px; height: 205px; }
  .card-front .brand-name { position: absolute; left: 24px; top: 30px; font-size: 23px; }
  .card-front .person { position: absolute; left: 26px; top: 82px; }
  .card-front .person h2 { font-size: 12px; font-weight: 700; color: var(--navy); }
  .card-front .person p { font-size: 9.5px; }
  .card-front .contacts { left: 26px; top: 128px; font-size: 9.5px; }
  .card-front .contacts li { gap: 5px; margin-bottom: 3px; }
  .card-front .address { right: 26px; top: 150px; font-size: 9.5px; }

  .card-back { left: 640px; top: 739px; width: 350px; height: 205px; }
  .card-back .brand-name {
    position: absolute; left: 0; right: 0; top: 82px;
    text-align: center; font-size: 26px;
  }
</style>
</head>
<body>

<svg width="0" height="0" style="position:absolute" aria-hidden="true">
  <defs>
    <symbol id="icon-phone" viewBox="0 0 14 14">
      <rect width="14" height="14" rx="2" fill="#1f50b8"/>
      <path d="M4 3.5 C3 5.5 6 10 9.5 10.5 L10.5 9.3 L8.8 8 L8 8.7 C6.9 8.2 5.8 7 5.4 6 L6 5.2 L5 3.4 Z" fill="#fff"/>
    </symbol>
    <symbol id="icon-mobile" viewBox="0 0 14 14">
      <rect width="14" height="14" rx="2" fill="#1f50b8"/>
      <rect x="4.5" y="2.5" width="5" height="9" rx="1" fill="#fff"/>
      <rect x="5.3" y="3.5" width="3.4" height="5" fill="#1f50b8"/>
    </symbol>
    <symbol id="icon-mail" viewBox="0 0 14 14">
      <rect width="14" height="14" rx="2" fill="#1f50b8"/>
      <rect x="3" y="4.5" width="8" height="5.5" fill="#fff"/>
      <path d="M3 4.5 L7 7.8 L11 4.5" fill="none" stroke="#1f50b8" stroke-width="1"/>
    </symbol>
    <symbol id="icon-web" viewBox="0 0 14 14">
      <rect width="14" height="14" rx="2" fill="#1f50b8"/>
      <circle cx="6" cy="6" r="2.6" fill="none" stroke="#fff" stroke-width="1.4"/>
      <path d="M8 8 L11 11" stroke="#fff" stroke-width="1.8"/>
    </symbol>
  </defs>
</svg>

<!-- Letterhead -->
<section class="sheet letterhead">
  <div class="brand-name">Bracken Ledger</div>
  <ul class="contacts">
    <li><svg width="14" height="14"><use href="#icon-phone"/></svg><span>(012) 345678</span></li>
    <li><svg width="14" height="14"><use href="#icon-mobile"/></svg><span>+44 700 9876543</span></li>
    <li><svg width="14" height="14"><use href="#icon-mail"/></svg><span>alex@<span class="hl">brackenledger</span>.com</span></li>
    <li><svg width="14" height="14"><use href="#icon-web"/></svg><i>www.<span class="hl">brackenledger</span>.com</i></li>
  </ul>
  <div class="address">dummy&nbsp; dummy<br>dummy dummy City<br>dummy Country</div>
  <svg class="band" height="22" viewBox="0 0 560 22" preserveAspectRatio="none" aria-hidden="true">
    <polygon points="0,0 368,0 388,22 0,22" fill="var(--navy)"/>
    <polygon points="378,0 560,0 560,22 398,22" fill="var(--blue)"/>
  </svg>
</section>

<!-- Compliment slip -->
<section class="sheet slip">
  <div class="brand-name">Bracken Ledger</div>
  <p class="greeting"><b>With</b> Compliments</p>
  <ul class="contacts">
    <li><svg width="12" height="12"><use href="#icon-phone"/></svg><span>(012) 345678</span></li>
    <li><svg width="12" height="12"><use href="#icon-mobile"/></svg><span>+44 700 9876543</span></li>
    <li><svg width="12" height="12"><use href="#icon-mail"/></svg><span>alex@<span class="hl">brackenledger</span>.com</span></li>
    <li><svg width="12" height="12"><use href="#icon-web"/></svg><i>www.<span class="hl">brackenledger</span>.com</i></li>
  </ul>
  <div class="address">dummy&nbsp; dummy<br>dummy dummy City<br>dummy Country</div>
  <svg class="band" height="16" viewBox="0 0 520 16" preserveAspectRatio="none" aria-hidden="true">
    <polygon points="0,0 360,0 374,16 0,16" fill="var(--navy)"/>
    <polygon points="368,0 520,0 520,16 382,16" fill="var(--blue)"/>
  </svg>
</section>

<!-- Business card front -->
<section class="sheet card-front">
  <div class="brand-name">Bracken Ledger</div>
  <div class="person">
    <h2>Alex MARLOW</h2>
    <p>Director</p>
  </div>
  <ul class="contacts">
    <li><svg width="11" height="11"><use href="#icon-phone"/></svg><span>(012) 345678</span></li>
    <li><svg width="11" height="11"><use href="#icon-mobile"/></svg><span>+44 700 9876543</span></li>
    <li><svg width="11" height="11"><use href="#icon-mail"/></svg><span>alex@<span class="hl">brackenledger</span>.com</span></li>
    <li><svg width="11" height="11"><use href="#icon-web"/></svg><i>www.<span class="hl">brackenledger</span>.com</i></li>
  </ul>
  <div class="address">dummy&nbsp; dummy<br>dummy dummy City<br>dummy Country</div>
  <svg class="band" height="12" viewBox="0 0 350 12" preserveAspectRatio="none" aria-hidden="true">
    <polygon points="0,0 212,0 224,12 0,12" fill="var(--navy)"/>
    <polygon points="219,0 350,0 350,12 231,12" fill="var(--blue)"/>
  </svg>
</section>

<!-- Business card back -->
<section class="sheet card-back">
  <div class="brand-name">Bracken Ledger</div>
</section>

</body>
</html>
```